Buchcover-Design für Fragenbuch
Ganz herzlichen Dank. Die Zusammenarbeit war völlig reibungslos und entspannt. Änderungswünsche wurden professionell umgesetzt und die kreativen Vorschläge fand ich super. Ich bin total glücklich mit dem Ergebnis.
Zielgruppe
Autorin und Workshopleiterin. Zielgruppe: Frauen ab 30
Aufgabenstellung
Ich benötige ein komplettes Buchcover, sowie 12 farbige Innenseiten. Es geht um ein Fragenbuch zum Ausfüllen mit dem Titel:
„Stärke jenes leise Herz
Das Arbeitsheft zum Eintragen für tiefere seelische Ruhe“
Das Format des Buches beträgt 17x22cm. Es ist in 12 Wochen unterteilt. Darum hätte ich gerne zwischen den einzelnen Wochen eine farbige Seite (1. Woche, 2. Woche etc.), die designmäßig mit dem Außencover korrespondiert.
Die Farben sollten eher zart oder gedeckt sein. Auf keinen Fall jedoch kitschig. Wichtig ist mir, dass keine bestimmte Person zu sehen ist. (Foto)
Das ist meine Website www.staerke-jenes-leise-herz.de

```html
<!DOCTYPE html>
<html lang="de">
<head>
<meta charset="utf-8">
<title>Stärke jenes leise Herz – Arbeitsheft</title>
<link href="https://fonts.googleapis.com/css2?family=EB+Garamond:wght@400;500&family=Open+Sans:wght@400;700&family=Allura&display=swap" rel="stylesheet">
<style>
  :root {
    --stage: #e4e3e1;
    --paper: #ffffff;
    --taupe: #cbbfb4;
    --taupe-light: #d7cdc3;
    --taupe-dark: #a59c95;
    --band: #bab0a8;
    --blush: #ddd2cc;
    --ink: #2a2826;
    --soft-white: #f1f0ee;
  }
  * { box-sizing: border-box; margin: 0; padding: 0; }
  html, body { width: 1200px; height: 960px; overflow: hidden; }
  body {
    background: var(--stage);
    font-family: "EB Garamond", Georgia, serif;
    color: var(--ink);
  }
  .layout {
    position: absolute; left: 40px; top: 247px;
    display: flex; gap: 40px;
  }
  .spread { display: flex; box-shadow: 0 6px 20px rgba(0,0,0,.12); }
  .page {
    position: relative; width: 360px; height: 466px; overflow: hidden;
  }

  /* Week divider page */
  .week-page { background: var(--taupe); }
  .week-tab {
    position: absolute; left: 60px; top: 0; width: 150px; height: 170px;
    background: var(--soft-white); border-radius: 0 0 75px 75px;
    text-align: center; padding-top: 44px; line-height: 1;
  }
  .week-number { font-size: 44px; display: block; }
  .week-label { font-size: 34px; letter-spacing: .02em; display: block; margin-top: 6px; }
  .module-headline {
    position: absolute; left: 0; right: 0; top: 205px;
    text-align: center; font-size: 21px; line-height: 1.12;
    text-transform: uppercase; letter-spacing: .02em;
  }
  .section-headline {
    position: absolute; left: 0; right: 0; top: 300px;
    text-align: center; font-size: 10px; letter-spacing: .06em;
    color: var(--paper); text-transform: uppercase;
  }
  .week-band {
    position: absolute; left: 0; right: 0; bottom: 0; height: 130px;
    background: var(--taupe-dark);
  }
  .arch-frame {
    position: absolute; left: 205px; bottom: 0; width: 120px; height: 150px;
    background: var(--soft-white); border-radius: 60px 60px 0 0;
  }
  .arch-image {
    position: absolute; left: 18px; right: 18px; top: 18px; bottom: 0;
    border-radius: 42px 42px 0 0;
    background: linear-gradient(180deg, #d9d8d6, #c4c2c0);
  }

  /* Content page */
  .content-page { background: var(--paper); }
  .photo-top {
    position: absolute; left: 55px; right: 18px; top: 36px; height: 190px;
    background: linear-gradient(135deg, #b69c86, #6f5647 60%, #9b8371);
  }
  .photo-bottom {
    position: absolute; left: 175px; right: 0; top: 232px; height: 180px;
    background: linear-gradient(160deg, #7a5a48, #3c2a22 70%);
  }
  .body-copy {
    position: absolute; left: 40px; top: 240px; width: 118px;
    font-family: "Open Sans", Arial, sans-serif; font-size: 7px; line-height: 1.55;
    color: #4a4542;
  }
  .body-rule { width: 34px; border-top: 1px solid #8a7d73; margin: 10px 0 8px; }
  .body-caption { font-weight: 700; color: #3a2a22; }
  .page-rule {
    position: absolute; left: 40px; right: 0; top: 440px;
    border-top: 1px solid #cfc8c2;
  }

  /* Cover */
  .cover { background: var(--taupe-light); box-shadow: 0 6px 20px rgba(0,0,0,.14); }
  .cover-arch {
    position: absolute; left: 40px; top: 0; width: 210px; height: 275px;
    border-radius: 0 0 105px 105px;
    background: linear-gradient(160deg, #eef0ef, #dfe4e3 55%, #e8e4e0);
  }
  .cover-band {
    position: absolute; left: 0; right: 0; top: 300px; bottom: 0;
    background: var(--band);
  }
  .cover-title {
    position: absolute; right: 26px; top: 195px;
    text-align: right; font-size: 30px; line-height: 1.08; font-weight: 500;
    text-transform: uppercase; letter-spacing: .01em;
  }
  .cover-subtitle {
    position: absolute; right: 26px; top: 300px;
    font-size: 28px; color: var(--paper);
  }
  .cover-tagline {
    position: absolute; left: 60px; right: 26px; top: 350px; height: 26px;
    background: var(--blush); color: var(--paper);
    font-size: 9px; letter-spacing: .05em; text-transform: uppercase;
    display: flex; align-items: center; justify-content: center;
  }
  .cover-author {
    position: absolute; left: 0; right: 0; top: 400px;
    text-align: center; font-family: "Allura", cursive; font-size: 22px;
  }
</style>
</head>
<body>
  <main class="layout">
    <section class="spread">
      <article class="page week-page">
        <div class="week-tab">
          <span class="week-number">1</span>
          <span class="week-label">WOCHE</span>
        </div>
        <h2 class="module-headline">Your module<br>headline comes<br>to here</h2>
        <p class="section-headline">Section headline</p>
        <div class="week-band"></div>
        <div class="arch-frame">
          <div class="arch-image" role="img" aria-label="Foto: Skulpturhand mit schwebendem goldenem Apfel"></div>
        </div>
      </article>

      <article class="page content-page">
        <div class="photo-top" role="img" aria-label="Foto: Blüten und Blätter in Sepiatönen"></div>
        <div class="photo-bottom" role="img" aria-label="Foto: dunkler Innenraum mit Wandleuchten"></div>
        <div class="body-copy">
          <p>Nimm dir jeden Tag ein paar Minuten Zeit für dich. Lies die Fragen in Ruhe und schreibe auf, was dir spontan einfällt. Es gibt kein richtig oder falsch, nur deine ehrliche Antwort.</p>
          <div class="body-rule"></div>
          <p class="body-caption">Schreib ehrlich und ohne Eile.</p>
        </div>
        <div class="page-rule"></div>
      </article>
    </section>

    <article class="page cover">
      <div class="cover-arch" role="img" aria-label="Foto: Jahresplaner und kupferfarbener Stift auf hellem Tisch"></div>
      <div class="cover-band"></div>
      <h1 class="cover-title">Stärke<br>jenes<br>leise Herz</h1>
      <p class="cover-subtitle">Das Arbeitsheft</p>
      <p class="cover-tagline">Zum Eintragen für tiefere seelische Ruhe</p>
      <p class="cover-author">by Lena Wirth</p>
    </article>
  </main>
</body>
</html>
```